Modernes Geschäftspapiere für Beratung zum Thema digitale Kommunikation & Zusammenarbeit
Zielgruppe
Beratung zum Thema digitale Kommunikation und Zusammenarbeit (z.B. Videoberatung, Chats, etc.).
Zielgruppe sind mittelständische und große Unternehmen sowie Behörden, Banken und Versicherungen.
Aufgabenstellung
Die Firmenfarbe ist HEX #6CC24A
Das Design sollte modern sein und nicht zu verspielt.
Das Design muss Platz bieten für alle relevanten Angaben einer GmbH (Adresse, Geschäftsführer, Kontaktmöglichkeiten, Registergericht und -nummer, Steuernummer und Bankverbindung)

```html
<!DOCTYPE html>
<html lang="de">
<head>
<meta charset="utf-8">
<title>Klarwerk Haus GmbH – Briefbogen</title>
<link href="https://fonts.googleapis.com/css2?family=Open+Sans:wght@400;600&display=swap" rel="stylesheet">
<style>
:root{
  --brand:#6CC24A;
  --brand-light:#a9d98f;
  --ink:#2b2b2b;
  --text:#3a3a3a;
  --muted:#777;
  --dark:#2a2a2a;
  --paper:#ffffff;
  --backdrop:#ececec;
  --faint:#f1f1f1;
}
*{margin:0;padding:0;box-sizing:border-box}
html,body{width:1200px;height:1010px;overflow:hidden;background:var(--backdrop);font-family:"Open Sans",Arial,sans-serif;color:var(--text)}
.letterhead{position:absolute;left:260px;top:24px;width:680px;height:962px;background:var(--paper);box-shadow:0 2px 10px rgba(0,0,0,.12);overflow:hidden}
.top-band{position:absolute;left:0;top:0;width:100%;height:7px;background:var(--brand)}
.brand{position:absolute;left:430px;top:70px;display:flex;align-items:center;gap:10px}
.brand-square{width:34px;height:34px;background:var(--brand);border-radius:6px}
.brand-name{font-size:26px;font-weight:400;color:var(--ink);letter-spacing:-.5px}
.contact{position:absolute;left:470px;top:130px;border-left:1px solid var(--ink);padding:4px 0 10px 12px;font-size:8.5px;line-height:1.35}
.contact .company{color:var(--brand);font-weight:600}
.contact ul{list-style:none;margin-top:8px}
.contact li{display:flex;align-items:center;gap:6px}
.contact svg{width:8px;height:8px;fill:var(--brand)}
.fold-mark{position:absolute;left:0;width:18px;height:1px;background:#bbb}
.sender-line{position:absolute;left:66px;top:240px;font-size:6.5px;border-bottom:1px solid var(--ink);padding-bottom:2px}
.sender-line .company{color:var(--brand);font-weight:600}
.recipient{position:absolute;left:66px;top:320px;font-size:11px;color:var(--ink)}
.body{position:absolute;left:66px;top:350px;width:440px;font-family:Arial,Helvetica,sans-serif;font-size:10.5px;line-height:1.3;color:var(--ink)}
.body p{margin-bottom:13px}
.signature{width:130px;height:34px;margin-top:16px;background:linear-gradient(90deg,#f4f4f4,#e6e6e6);border-radius:3px}
.watermark{position:absolute;left:330px;top:560px;font-size:54px;color:var(--faint);letter-spacing:-1px;white-space:nowrap}
.watermark-square{position:absolute;left:350px;top:640px;width:150px;height:150px;background:var(--faint);border-radius:18px}
.footer-art{position:absolute;left:0;bottom:0;width:680px;height:220px}
.bank{position:absolute;left:38px;bottom:70px;display:flex;gap:14px;font-size:8.5px;line-height:1.35;color:var(--ink)}
.bank .col{padding-left:12px;border-left:1px solid var(--brand)}
.bank .col:first-child{border-left:none;padding-left:0}
.website{position:absolute;right:26px;bottom:22px;font-size:11px;color:#fff}
</style>
</head>
<body>
<main class="letterhead">
  <div class="top-band"></div>

  <header>
    <div class="brand"><span class="brand-square"></span><span class="brand-name">KlarwerkHaus</span></div>
    <address class="contact">
      <div class="company">Klarwerk Haus GmbH</div>
      <div>Lindenhofweg 14</div>
      <div>90431 Nordheim</div>
      <ul>
        <li><svg viewBox="0 0 10 10"><path d="M2 1l2 2-1 1c1 2 2 3 3 3l1-1 2 2-1 2C4 10 0 6 0 2z"/></svg>(0911) 450 61 27 3</li>
        <li><svg viewBox="0 0 10 10"><rect x="1" y="3" width="8" height="5"/><rect x="3" y="1" width="4" height="2"/></svg>(0911) 450 61 27 4</li>
        <li><svg viewBox="0 0 10 10"><rect x="2.5" y="0" width="5" height="10" rx="1"/></svg>(0171) 384 66 19</li>
        <li><svg viewBox="0 0 10 10"><rect x="0" y="2" width="10" height="6"/></svg>info@klarwerkhaus.de</li>
        <li><svg viewBox="0 0 10 10"><circle cx="5" cy="5" r="5"/></svg>support.klarwerkhaus.de</li>
      </ul>
    </address>
  </header>

  <div class="fold-mark" style="top:340px"></div>
  <div class="fold-mark" style="top:660px"></div>

  <div class="sender-line"><span class="company">Klarwerk Haus GmbH</span> | Lindenhofweg 14 | 90431 Nordheim</div>

  <div class="recipient">Herr Lindqvist</div>

  <section class="body">
    <p>Lorem ipsum dolor sit amet, consectetur adipiscing elit. Proin tincidunt, lectus id malesuada cursus, lorem augue egestas magna, ut mattis orci ante ut arcu. Sed mauris tellus, fermentum quis ligula nec, posuere pulvinar eros. Nam at mi quis velit pellentesque finibus. Donec lacus velit, faucibus mollis dolor nec, finibus pellentesque orci. Duis sed dictum elit, ut posuere arcu. Phasellus ac dolor et ante consequat rutrum nec nec tortor. Donec consequat, nibh sit amet pulvinar faucibus, turpis magna venenatis diam, vel pretium eros erat vestibulum nulla.</p>
    <p>Sed pretium ac enim eu viverra. Aliquam ac est eget magna convallis convallis. Aenean augue purus, finibus eget turpis quis, finibus dignissim nibh. Phasellus viverra lobortis dignissim. Duis varius turpis in sapien accumsan facilisis. Sed vehicula gravida diam a interdum. Nullam convallis ligula id erat egestas consequat. Integer consectetur ex vel aliquet iaculis. Vestibulum molestie sodales mauris, at tincidunt risus pellentesqu.</p>
    <p>Mauris facilisis, lectus at accumsan tincidunt, dui magna imperdiet sem, quis tempor est lectus eu ipsum. Praesent in fermentum nisl. Maecenas at lorem at odio interdum iaculis. Pellentesque cursus nulla nunc, ut suscipit nulla maximus et. Donec maximus rhoncus metus, vel laoreet nisi pretium sit amet. Donec posuere enim lectus, vitae aliquam augue tincidunt dignissim. Morbi vitae congue velit, quis elementum.</p>
    <div class="signature" role="img" aria-label="Handschriftliche Unterschrift"></div>
  </section>

  <div class="watermark-square"></div>
  <div class="watermark">KlarwerkHaus</div>

  <svg class="footer-art" viewBox="0 0 680 220" preserveAspectRatio="none" aria-hidden="true">
    <path d="M0 220 L0 206 C260 196 520 130 680 40 L680 220 Z" fill="var(--dark)"/>
    <path d="M60 200 C300 170 520 110 620 50 C540 120 320 185 60 200 Z" fill="var(--brand)"/>
  </svg>

  <footer>
    <div class="bank">
      <div class="col">Bankverbindung:<br>Jonas Velder</div>
      <div class="col">Nordmark Bank<br>USt-ID-Nr. DEXXXXXXX</div>
      <div class="col">IBAN: DEXX XXXX XXXX XXXX XXXX X<br>BIC: XXXXXXXX</div>
    </div>
    <div class="website">www.klarwerkhaus.de</div>
  </footer>
</main>
</body>
</html>
```